I will ask the design of the business card

We are looking for business card design of the new company "VORTELL PAYWORKS STUDIO LLC." Based in Azerbaijan.
In case
We are working on Azerbaijan to set up the first exchange of crypto currencies.

The key currency used in exchanges is called "MIRTA".
In case
We are doing project to make crypto currency infrastructure.

We provide state-of-the-art technology to the world.

```html
<!DOCTYPE html>
<html lang="en">
<head>
<meta charset="utf-8">
<title>Vortell Payworks Studio – Business Card</title>
<link rel="stylesheet" href="https://fonts.googleapis.com/css2?family=Oswald:wght@600&family=Open+Sans:wght@400;700&family=Roboto:wght@400&display=swap">
<style>
  :root {
    --backdrop: #666666;
    --navy: #063a5e;
    --green: #86a33a;
    --paper: #ffffff;
    --ink: #3a3a3a;
    --rule: #c9c9c9;
  }
  * { margin: 0; padding: 0; box-sizing: border-box; }
  html, body { width: 1200px; height: 802px; overflow: hidden; }
  body { background: var(--backdrop); position: relative; font-family: "Open Sans", sans-serif; }

  .card { position: absolute; top: 274px; width: 442px; height: 265px; }
  .card-front { left: 136px; background: var(--paper); }
  .card-back { left: 624px; background: var(--navy); }

  .wordmark {
    position: absolute;
    font-family: "Oswald", sans-serif;
    font-weight: 600;
    text-transform: uppercase;
    line-height: 1.02;
  }
  .wordmark-line { display: block; }
  .wordmark-square { display: inline-block; background: var(--green); vertical-align: middle; }

  .card-front .wordmark { left: 37px; top: 80px; width: 176px; color: var(--navy); font-size: 26px; }
  .card-front .wordmark-square { width: 14px; height: 14px; margin-right: 8px; margin-top: -4px; }

  .card-back .wordmark { left: 0; right: 0; top: 64px; text-align: center; color: var(--paper); font-size: 40px; }
  .card-back .wordmark-square { width: 20px; height: 20px; margin-right: 12px; margin-top: -6px; }

  .divider { position: absolute; left: 225px; top: 58px; width: 1px; height: 138px; background: var(--rule); }

  .contact { position: absolute; left: 244px; top: 62px; }
  .person-name { font-size: 16px; font-weight: 700; letter-spacing: 0.2px; line-height: 1.2; }
  .person-name .given { color: var(--green); }
  .person-name .family { color: var(--navy); }
  .person-role { font-family: "Roboto", sans-serif; font-size: 12.5px; color: var(--ink); margin-bottom: 9px; }

  .contact-list { list-style: none; font-family: "Roboto", sans-serif; font-size: 12.5px; color: var(--ink); }
  .contact-list li { display: flex; align-items: center; height: 16px; }
  .contact-list svg { width: 10px; height: 10px; margin-right: 4px; fill: var(--green); flex: none; }

  .address { margin-top: 6px; font-size: 12.5px; line-height: 1.27; color: var(--ink); }
</style>
</head>
<body>

<section class="card card-front" aria-label="Business card front">
  <div class="wordmark">
    <span class="wordmark-line">Vortell</span>
    <span class="wordmark-line">Payworks</span>
    <span class="wordmark-line"><span class="wordmark-square"></span>Studio LLC.</span>
  </div>

  <div class="divider"></div>

  <div class="contact">
    <p class="person-name"><span class="given">DARIEN</span> <span class="family">KOLAS</span></p>
    <p class="person-role">Managing Director</p>
    <ul class="contact-list">
      <li><svg viewBox="0 0 10 10" aria-hidden="true"><path d="M1 3.5C1 2 2.5 1.5 5 1.5S9 2 9 3.5V4.3H7V3.4H3V4.3H1Z M2 5H8L9 9H1Z"/></svg>012-555 0190</li>
      <li><svg viewBox="0 0 10 10" aria-hidden="true"><path d="M2.5 0.5H7.5V9.5H2.5Z M3.3 1.5V7.5H6.7V1.5Z M4.5 8H5.5V9H4.5Z" fill-rule="evenodd"/></svg>012-555 0191</li>
      <li><svg viewBox="0 0 10 10" aria-hidden="true"><path d="M0.5 2H9.5V8.5H0.5Z M1.3 2.8L5 5.6L8.7 2.8Z" fill-rule="evenodd"/></svg>info@vortellpay.com</li>
      <li><svg viewBox="0 0 10 10" aria-hidden="true"><circle cx="5" cy="5" r="4.5"/></svg>www.vortellpay.com</li>
    </ul>
    <p class="address">12345, Address Goes Here<br>Country Name, 123456.</p>
  </div>
</section>

<section class="card card-back" aria-label="Business card back">
  <div class="wordmark">
    <span class="wordmark-line">Vortell</span>
    <span class="wordmark-line">Payworks</span>
    <span class="wordmark-line"><span class="wordmark-square"></span>Studio LLC.</span>
  </div>
</section>

</body>
</html>
```